Premium Juice and Wine Bottle Label

We require a premium label design for a Burgundy style wine bottle - the design should reflect pure and organic theme, with a reference to New Zealand blueberries. The winning design will look high-end, simple but sophisticated. Our logo is attached, refer :

https://www.orvalecellars.co.nz and https://www.pirovane.co.nz/wines/details/coming-soon-showcase/2018

for inspiration.

Target Market(s)

High-end retail grocery stores, wine shops, bars.

Requirements
Must have
• Label should leave enough space for barcode and nutrients/ingredients etc. Reference to New Zealand, natural-beverage, be very high-end in design. Refer links in project description for inspiration. Refer to attached logo, which must be used - feel free to change colour in order to obtain the best high-class design.
Nice to have
• N/A.
Should not have
• Cartoons or pictures of berries.

```html
<!DOCTYPE html>
<html lang="en">
<head>
<meta charset="utf-8">
<title>Tallow Lane Pinot Noir Label</title>
<link href="https://fonts.googleapis.com/css2?family=Cormorant+SC:wght@500;600&display=swap" rel="stylesheet">
<style>
  :root {
    --backdrop: #f2f2f2;
    --charcoal: #1d2427;
    --burgundy: #6e1713;
    --copper: #b46546;
    --copper-light: #cb8d6c;
    --ink: #f6f2ee;
  }
  * { margin: 0; padding: 0; box-sizing: border-box; }
  html, body {
    width: 830px;
    height: 1200px;
    overflow: hidden;
    background: var(--backdrop);
  }
  .canvas {
    position: relative;
    width: 830px;
    height: 1200px;
  }
  .label {
    position: absolute;
    left: 85px;
    top: 110px;
    width: 660px;
    height: 980px;
    background: linear-gradient(90deg,
      var(--charcoal) 0%,
      var(--charcoal) 8%,
      #3a1d1c 22%,
      var(--burgundy) 36%,
      var(--copper) 58%,
      var(--copper) 82%,
      var(--copper-light) 100%);
    font-family: "Cormorant SC", "Times New Roman", serif;
    color: var(--ink);
  }
  .brand {
    position: absolute;
    left: 0;
    right: 0;
    top: 330px;
    display: flex;
    align-items: center;
    justify-content: center;
    gap: 18px;
  }
  .brand-square {
    width: 34px;
    height: 34px;
    border: 4px solid var(--ink);
  }
  .brand-name {
    font-size: 64px;
    font-weight: 600;
    letter-spacing: 3px;
    line-height: 1;
  }
  .varietal {
    position: absolute;
    left: 0;
    right: 0;
    top: 796px;
    text-align: center;
    font-size: 34px;
    font-weight: 600;
    letter-spacing: 6px;
  }
  .divider {
    position: absolute;
    left: 170px;
    width: 400px;
    top: 846px;
    height: 1px;
    background: var(--ink);
    opacity: 0.8;
  }
  .region {
    position: absolute;
    left: 0;
    right: 0;
    top: 862px;
    text-align: center;
    font-size: 26px;
    font-weight: 500;
    letter-spacing: 9px;
  }
</style>
</head>
<body>
  <main class="canvas">
    <section class="label">
      <div class="brand">
        <span class="brand-square"></span>
        <span class="brand-name">Tallow Lane</span>
      </div>
      <p class="varietal">Pinot Noir</p>
      <div class="divider"></div>
      <p class="region">New Zealand</p>
    </section>
  </main>
</body>
</html>
```